Book Cover for Luminous Framework: The Unfolding of Awareness

We are looking for a cover design for a new book by Marla Pettigrew that explores her unique mind-body-spirit approach to physical healing modalities. The approach combines insights from Yoga, chiropractic, and other healing arts to help re-align the body in order to allow energy to flow more freely through the body.

We are looking for a front cover, back cover, and spine; and we would potentially be interested in having the interior laid out as well (if that's within your skill set).

You can check out the author's website to get a better sense of the material and also some of the visual elements that appeal to us (www.velantrisight).

Also, I've attached a very rough version of the intro to the book and chapter 1 to give you a sense of the material.

Target Market(s)

yoga, spiritual, body work

Industry/Entity Type

Book Publisher

Requirements
Must have
• Bright colors, body images, depth.
Nice to have
• Looking for a combination of spirituality and science. The book is an approach that integrates both modalities, so the aesthetic should reflect this. On the science side, we are looking for images of the body, things that convey structure, etc.
Should not have
• We want something that conveys spirituality/depth, but doesn't come across as too new agey.

```html
<!DOCTYPE html>
<html lang="en">
<head>
<meta charset="utf-8">
<title>Luminous Framework — Book Cover Spread</title>
<link rel="stylesheet" href="https://fonts.googleapis.com/css2?family=EB+Garamond:ital,wght@0,400;1,400;1,600&family=Montserrat:wght@700&family=Oswald:wght@400&display=swap">
<style>
  :root {
    --paper: #ffffff;
    --sky-dark: #2e1a0c;
    --cloud-brown: #5a3316;
    --sun-gold: #f6b040;
    --sun-core: #ffe39a;
    --sea-dark: #3a2412;
    --sand-amber: #b8661e;
    --ink-white: #ffffff;
    --copy-cream: #fff3e2;
    --ink-black: #111111;
    --imprint-gold: #d99a3c;
    --spine-brown: #3b1f10;
    --spine-orange: #d0741f;
    --spine-rust: #8a3e14;
  }
  * { box-sizing: border-box; margin: 0; padding: 0; }
  html, body {
    width: 1200px; height: 914px; overflow: hidden;
    background: var(--paper);
  }
  .spread { position: relative; width: 1200px; height: 914px; }
  .panel { position: absolute; top: 29px; height: 857px; overflow: hidden; }
  .back-cover { left: 29px; width: 514px; }
  .spine { left: 571px; width: 58px; background: var(--paper); }
  .front-cover { left: 657px; width: 514px; }
  .cover-art, .cover-type { position: absolute; inset: 0; width: 100%; height: 100%; }

  .back-copy {
    position: absolute; left: 29px; top: 168px; width: 462px;
    font-family: "EB Garamond", Georgia, serif;
    font-size: 15.6px; line-height: 25.5px;
    color: var(--copy-cream);
  }
  .back-copy p + p { text-indent: 24px; }

  .imprint-mark {
    position: absolute; left: 19px; top: 751px;
    display: flex; align-items: center; gap: 14px;
  }
  .imprint-dot {
    width: 60px; height: 60px; border-radius: 50%;
    border: 2.5px solid var(--ink-white);
  }
  .imprint-name {
    font-family: "EB Garamond", Georgia, serif;
    font-size: 17px; line-height: 25px; letter-spacing: 0.5px;
    color: var(--ink-white);
  }
  .isbn-box {
    position: absolute; left: 298px; top: 733px; width: 202px; height: 87px;
    background: var(--paper);
  }

  .title-main { font-family: "Oswald", "Arial Narrow", sans-serif; font-weight: 400; fill: var(--ink-white); }
  .title-sub { font-family: "EB Garamond", Georgia, serif; font-style: italic; fill: var(--ink-black); }
  .author-name { font-family: "Montserrat", Arial, sans-serif; font-weight: 700; fill: var(--ink-white); }
  .imprint-line { font-family: "EB Garamond", Georgia, serif; font-style: italic; font-weight: 600; fill: var(--imprint-gold); }
  .spine-type { font-family: "Montserrat", Arial, sans-serif; font-weight: 700; }
</style>
</head>
<body>
<main class="spread">

  <!-- Back cover -->
  <section class="panel back-cover">
    <svg class="cover-art" viewBox="0 0 514 857" preserveAspectRatio="none" role="img" aria-label="Sunset photograph over a calm sea and wet sand beach, glowing orange sky">
      <defs>
        <linearGradient id="backSky" x1="0" y1="0" x2="0" y2="1">
          <stop offset="0" stop-color="#2c190b"/>
          <stop offset="0.2" stop-color="#6a3a17"/>
          <stop offset="0.42" stop-color="#c7741f"/>
          <stop offset="0.52" stop-color="#e89a34"/>
          <stop offset="0.56" stop-color="#4a2c14"/>
          <stop offset="0.62" stop-color="#7a4318"/>
          <stop offset="0.78" stop-color="#a95e1c"/>
          <stop offset="0.9" stop-color="#5a3112"/>
          <stop offset="1" stop-color="#2a170a"/>
        </linearGradient>
        <radialGradient id="backGlow" cx="0.92" cy="0.5" r="0.55">
          <stop offset="0" stop-color="#ffd27a" stop-opacity="0.85"/>
          <stop offset="0.5" stop-color="#f2a43a" stop-opacity="0.35"/>
          <stop offset="1" stop-color="#f2a43a" stop-opacity="0"/>
        </radialGradient>
      </defs>
      <rect width="514" height="857" fill="url(#backSky)"/>
      <rect width="514" height="857" fill="url(#backGlow)"/>
    </svg>

    <div class="back-copy">
      <p>Anducit resed modita si rem rerum volupti bearchi ciminimus et aut mo berferferia ilitatur rernatempos voluptatusam voluptatur? Labo. Iquias aliqui cum que vid exceped minventurio omnistis reium, simusda doluptati quia int qui temquodipis et utem de comnime ndellenet, sa evel est, secus acest molore paruptate volupta tectioribus re volore, eum cuptur? Uda net fugitibus istrum rem dolorrum, conem voleste et essi cuptat.</p>
      <p>Ilia nonseceat ullorpo rectes sit arum nescillitate et endis as magniss imporis alicium et exerume excepera dolorerumeni ad mod que volorem inciet aut voluptiam quunt a dolut ut et repero de lit fugitat emporum ad eum eum fugita duntem liquod que apitatis et fugit, samusdae. Imi, nobit et mos nonseque natur sandis quam dios ad que voloren isciatem. Itatemo luptae. Lescimu sciendi tasinventem que venimusae dolentem ad maior soluptate non nis nonseque pro ipsam, officil icipsum nest lanto venisci pitiorias susda dolorep tatur, odi arciume erios etur aboris iuntio. Itat et quia am fugiat landisquo mi, se laborem oluptatem volor-</p>
    </div>

    <div class="imprint-mark">
      <span class="imprint-dot"></span>
      <span class="imprint-name">VELANTRI<br>SIGHT</span>
    </div>

    <div class="isbn-box"></div>
  </section>

  <!-- Spine -->
  <section class="panel spine">
    <svg class="cover-type" viewBox="0 0 58 857">
      <defs>
        <linearGradient id="spineInk" x1="0" y1="0" x2="1" y2="0">
          <stop offset="0" stop-color="var(--spine-rust)"/>
          <stop offset="1" stop-color="var(--spine-orange)"/>
        </linearGradient>
      </defs>
      <rect class="spine-cap" x="0" y="0" width="58" height="76" fill="var(--spine-brown)"/>
      <text class="spine-type" transform="translate(15 103) rotate(90)" font-size="41" textLength="252" lengthAdjust="spacingAndGlyphs" fill="url(#spineInk)">LUMINOUS</text>
      <text class="spine-type" transform="translate(35 391) rotate(90)" font-size="17" textLength="56" lengthAdjust="spacingAndGlyphs" fill="var(--spine-orange)">MARLA</text>
      <text class="spine-type" transform="translate(14 391) rotate(90)" font-size="17" textLength="100" lengthAdjust="spacingAndGlyphs" fill="var(--spine-orange)">PETTIGREW</text>
      <text class="spine-type" transform="translate(15 511) rotate(90)" font-size="41" textLength="248" lengthAdjust="spacingAndGlyphs" fill="url(#spineInk)">FRAMEWORK</text>
      <rect class="spine-cap" x="0" y="781" width="58" height="76" fill="var(--spine-brown)"/>
      <circle cx="29" cy="819" r="14" fill="none" stroke="var(--ink-white)" stroke-width="2"/>
    </svg>
  </section>

  <!-- Front cover -->
  <section class="panel front-cover">
    <svg class="cover-art" viewBox="0 0 514 857" preserveAspectRatio="none" role="img" aria-label="Sunset photograph of a beach with a silhouetted seated figure raising both arms toward the glowing sky">
      <defs>
        <linearGradient id="frontSky" x1="0" y1="0" x2="0" y2="1">
          <stop offset="0" stop-color="#2a170a"/>
          <stop offset="0.18" stop-color="#4e2c13"/>
          <stop offset="0.36" stop-color="#b8661c"/>
          <stop offset="0.48" stop-color="#efa236"/>
          <stop offset="0.545" stop-color="#f6b24a"/>
          <stop offset="0.56" stop-color="#3e2512"/>
          <stop offset="0.62" stop-color="#6c3b16"/>
          <stop offset="0.72" stop-color="#c67322"/>
          <stop offset="0.86" stop-color="#7c4317"/>
          <stop offset="1" stop-color="#26150a"/>
        </linearGradient>
        <radialGradient id="frontSun" cx="0.18" cy="0.42" r="0.5">
          <stop offset="0" stop-color="#fff0b8" stop-opacity="0.95"/>
          <stop offset="0.35" stop-color="#f8bb52" stop-opacity="0.55"/>
          <stop offset="1" stop-color="#f8bb52" stop-opacity="0"/>
        </radialGradient>
      </defs>
      <rect width="514" height="857" fill="url(#frontSky)"/>
      <rect width="514" height="857" fill="url(#frontSun)"/>
    </svg>

    <svg class="cover-type" viewBox="0 0 514 857" aria-label="Luminous Framework: The Unfolding of Awareness by Marla Pettigrew">
      <text class="title-main" x="17" y="151" font-size="150" textLength="482" lengthAdjust="spacingAndGlyphs">LUMINOUS</text>
      <text class="title-main" x="17" y="283" font-size="150" textLength="482" lengthAdjust="spacingAndGlyphs">FRAMEWORK</text>
      <text class="title-sub" x="65" y="379" font-size="50" textLength="390" lengthAdjust="spacingAndGlyphs">The Unfolding</text>
      <text class="title-sub" x="65" y="443" font-size="50" textLength="386" lengthAdjust="spacingAndGlyphs">of Awareness</text>
      <text class="author-name" x="47" y="797" font-size="40" textLength="422" lengthAdjust="spacingAndGlyphs">MARLA PETTIGREW</text>
      <text class="imprint-line" x="257" y="835" font-size="20" text-anchor="middle" letter-spacing="0.5">Velantri Sight</text>
    </svg>
  </section>

</main>
</body>
</html>
```